Vorrel Letterhead

Need a fresh looking design. We are a IT service company and I would like some elements of the logo to flow through. I have included the logo as an attachment. I have also included business card design as it might help with the design.

Industry/Entity Type

Business

```html
<!DOCTYPE html>
<html lang="en">
<head>
<meta charset="utf-8">
<title>Vorrel Letterhead</title>
<link href="https://fonts.googleapis.com/css2?family=Open+Sans:wght@400;600;700&display=swap" rel="stylesheet">
<style>
  :root {
    --charcoal: #2f2f2f;
    --green: #8cc63f;
    --green-dark: #6aa82a;
    --green-soft: #b5d98a;
    --text: #222222;
    --paper: #ffffff;
  }
  * { margin: 0; padding: 0; box-sizing: border-box; }
  html, body { width: 849px; height: 1200px; overflow: hidden; background: var(--paper); }
  .letterhead {
    position: relative;
    width: 849px;
    height: 1200px;
    font-family: "Open Sans", Arial, sans-serif;
    color: var(--text);
    overflow: hidden;
  }
  .header-shapes { position: absolute; top: 0; left: 0; }
  .contact-block {
    position: absolute;
    top: 30px;
    left: 40px;
    width: 210px;
    text-align: right;
    color: #ffffff;
    font-size: 14px;
    line-height: 19px;
    font-weight: 600;
  }
  .brand-name {
    position: absolute;
    top: 30px;
    left: 272px;
    font-size: 62px;
    font-weight: 700;
    color: #ffffff;
    line-height: 1;
  }
  .website {
    position: absolute;
    top: 68px;
    left: 603px;
    font-size: 15px;
    font-weight: 600;
    color: var(--green-dark);
  }
  .letter-body {
    position: absolute;
    top: 318px;
    left: 99px;
    width: 672px;
    font-size: 11.6px;
    line-height: 17.6px;
  }
  .letter-body p { margin: 0; }
  .closing {
    position: absolute;
    top: 792px;
    left: 99px;
    font-size: 12px;
    font-weight: 700;
  }
  .signature-row {
    position: absolute;
    top: 876px;
    left: 99px;
    display: flex;
    align-items: center;
    gap: 28px;
  }
  .signature-label { font-size: 11px; font-weight: 700; }
  .signature-area {
    width: 190px;
    height: 46px;
    background: linear-gradient(90deg, #e6e6e6, #f5f5f5);
  }
  .footer-rule {
    position: absolute;
    top: 1156px;
    height: 3px;
  }
  .footer-rule.dark { left: 0; width: 360px; background: var(--charcoal); }
  .footer-rule.green { left: 778px; width: 71px; background: var(--green); }
  .footer-address {
    position: absolute;
    top: 1145px;
    left: 510px;
    width: 262px;
    text-align: center;
    font-size: 15px;
    font-weight: 700;
  }
</style>
</head>
<body>
<div class="letterhead">
  <svg class="header-shapes" width="849" height="200" viewBox="0 0 849 200" aria-hidden="true">
    <path d="M0 0 H552 V100 Q420 132 250 134 Q120 136 0 128 Z" fill="var(--charcoal)"/>
    <path d="M552 0 H849 V30 Q760 106 552 100 Z" fill="var(--green)"/>
    <path d="M552 100 Q760 106 849 30 V40 Q770 118 552 108 Z" fill="var(--green-soft)"/>
  </svg>

  <div class="contact-block">
    <div>Mobile: 0491 552 108</div>
    <div>Phone: 02 5550 1834</div>
    <div>Fax: 02 5550 1835</div>
    <div>email: tj@vorrel.com.au</div>
  </div>

  <div class="brand-name">Vorrel</div>

  <div class="website">www.vorrel.com.au</div>

  <div class="letter-body">
    <p>A letterhead is the banner at the top of a sheet of letter used for official correspondence when sending them out. It usually consists of contact information of the company like name, address logo or corporate design and sometimes a background.</p>
    <p>A letterhead is the banner at the top of a sheet of letter used for official correspondence when sending them out. It usually consists of contact information of the company like name, address logo or corporate design and sometimes a background.</p>
    <p>A letterhead is the banner at the top of a sheet of letter used for official correspondence when sending them out. It usually consists of contact information of the company like name, address logo or corporate design and sometimes a background.</p>
    <p>A letterhead is the banner at the top of a sheet of letter used for official correspondence when sending them out. It usually consists of contact information of the company like name, address logo or corporate design and sometimes a background.</p>
    <p>A letterhead is the banner at the top of a sheet of letter used for official correspondence when sending them out. It usually consists of contact information of the company like name, address logo or corporate design and sometimes a background.</p>
    <p>A letterhead is the banner at the top of a sheet of letter used for official correspondence when sending them out. It usually consists of contact information of the company like name, address logo or corporate design and sometimes a background.</p>
    <p>A letterhead is the banner at the top of a sheet of letter used for official correspondence when sending them out. It usually consists of contact information of the company like name, address logo or corporate design and sometimes a background.</p>
  </div>

  <div class="closing">Faithfully,</div>

  <div class="signature-row">
    <span class="signature-label">Sign</span>
    <div class="signature-area" role="img" aria-label="Handwritten signature"></div>
  </div>

  <div class="footer-rule dark"></div>
  <div class="footer-address">P.O Box 4410, Marrick 2094</div>
  <div class="footer-rule green"></div>
</div>
</body>
</html>
```